Website design for Cambridge based systematic hedge fund

We have run previous craftmosaic competitions to design our company logo, business cards and the styling of our presentation deck (see attached files).
As the final step we are looking to get a website designed that is thematically consistent with these existing elements of our branding.
You can find some of our competitors websites below:
https://www.quelmarsh.example/
https://www.fenloor.example/
https://www.pyvart.example/
https://www.dulvet.example/
https://www.orbelmfunds.example/
https://www.valtrigo.example/
https://www.meskilfunds.example/home
We would like to have a website that works well on both mobile devices and desktops. Either just as one page that can be scrolled down, with links at the top that skips to certain sections, or a few separate pages that can be navigated by a top menu.
It should look professional, we are not after lots of animations or unnecessary transitions, and in particular the website must be smooth to navigate. We would like to avoid having peoples of people, we are happy to make use of elements from the presentation (for example the style of the cover slide, or the section slides with the faded bridge in the background), or 'financial' style images.
We would like to have the following sections for now. For some of these some example text has been provided, final text may change but it will be of similar length. For the other sections we are happy to just have template text for now. At the moment we are mainly interested to see styles/layouts as words can be added easily afterwards:
1) We will need a disclaimer pop up the first time someone visits the site (see for example the meskilfunds example).
2) Top page - company name, then in larger text "Bringing AI and Statistical Inference to Financial Markets", and somewhere in smaller text "Harlow Vectors is a quantitative asset manager with the singular focus of delivering algorithmic strategies that work"
3) "About us" section: will describe us as a company, details our approach, company values, and explains the company logo.
Example text:
"We deliver consistent alpha across liquid markets through the application of proprietary IP in Bayesian inference, machine learning and artificial intelligence. We are a multi-disciplinary team founded by experienced finance professionals from premier institutions, leading academics from the Thornbury Stellar Unit at Ashmere College and world-class software engineers.
Our logo portrays a sillhoute of the lattice walkway at Ashmere College. Our unique scientific approach allows us to bridge cutting-edge mathematical research and computing expertise with financial knowledge to bring algorithmns that work to liquid markets"
4) Hiring section, detailing our culture, what we are looking for.
Example text:
"We are always looking for exceptional talent to join our entrepreneurial team. We are looking for individuals who are creative thinkers, can demonstrate analytical rigour and are passionate about the intersection of science, finance and technology.
We prioritise having a company culture that promotes sharing ideas in a safe, collaborative research environment. We make sure that every member of the team has the oppertunity to explore their own ideas through weekly 'innovation time', and ensure that everyone gets the support they need to continue to grow as individuals within the company."
5) A section for news/press releases
6) Contact us area at the bottom with office location and email. We will need to list 3 addresses for our Cambridge, London and Singapore offices, along with a couple of contact emails or phone numbers
7) A client login button at the top that will take them to a different website (unrelated to this one).

```html
<!DOCTYPE html>
<html lang="en">
<head>
<meta charset="utf-8">
<title>Harlow Vectors – Systematic Hedge Fund</title>
<link href="https://fonts.googleapis.com/css2?family=Jost:wght@400;500;600&display=swap" rel="stylesheet">
<style>
:root{
  --navy-deep:#041a30;
  --navy:#06203b;
  --brand-blue:#0b3e6f;
  --mid-blue:#3a7ccc;
  --light-blue:#a9c9ee;
  --mauve:#9c6179;
  --plum:#8e5471;
  --paper:#ffffff;
  --mist:#f3f4f6;
  --ink:#3b3f45;
  --cyan:#2de0e6;
}
*{box-sizing:border-box;margin:0;padding:0}
html,body{width:1200px;height:3652px;overflow:hidden}
body{font-family:"Jost",sans-serif;color:var(--ink);background:var(--paper);position:relative}
.abs{position:absolute}
section,footer,header{position:absolute;left:0;width:1200px;overflow:hidden}

/* hero */
.hero{top:0;height:673px;background:radial-gradient(circle at 70% 45%,#0a2d4f 0%,var(--navy) 55%,#041a30 100%)}
.brand-mark{color:#fff;font-weight:600;line-height:1}
.hero .brand-mark{left:173px;top:50px;font-size:25px;letter-spacing:1px}
.hero .brand-mark small{display:block;font-size:13px;letter-spacing:9px;margin-top:6px;font-weight:500}
.main-nav{left:476px;top:44px;display:flex;gap:20px}
.main-nav a{color:#fff;text-decoration:none;font-size:15px;letter-spacing:.2px}
.btn-login{left:914px;top:28px;width:112px;height:53px;background:var(--mauve);color:#fff;font-size:15px;font-weight:500;display:flex;align-items:center;justify-content:center;text-decoration:none}
.hero-title{left:173px;top:198px;color:#fff;font-weight:600;line-height:1.1}
.hero-title .small{font-size:47px;display:block}
.hero-title .big{font-size:59px;display:block}
.hero-lede{left:173px;top:336px;width:420px;color:#fff;font-size:17.5px;line-height:30px}
.slider-dots{left:173px;top:432px;display:flex;gap:7px}
.slider-dots span{width:15px;height:15px;border-radius:50%;background:#3a5876}
.slider-dots span:first-child{background:#fff}
.globe{left:632px;top:158px;width:380px;height:370px;border-radius:50%;background:radial-gradient(circle at 50% 45%,rgba(45,224,230,.55) 0%,rgba(20,140,170,.35) 45%,rgba(6,32,59,0) 72%)}

/* shared type */
.kicker{font-size:19px;font-weight:500;color:var(--brand-blue);line-height:1}
.heading{font-size:35px;font-weight:400;color:var(--brand-blue);line-height:1.1;margin-top:6px}
.body-copy{font-size:12.5px;line-height:22.5px;color:var(--ink);text-align:justify}
.btn-more{display:flex;align-items:center;justify-content:center;width:103px;height:52px;background:var(--mauve);color:#fff;font-size:15px;font-weight:500;text-decoration:none}

/* about */
.about{top:673px;height:547px;background:var(--paper)}
.bridge-art{left:0;top:117px;width:570px;height:300px;background:linear-gradient(160deg,rgba(11,62,111,.0) 10%,rgba(11,62,111,.18) 45%,rgba(169,201,238,.45) 75%,rgba(255,255,255,0) 95%);border-radius:0 60% 40% 0}
.about .text{left:638px;top:110px;width:390px}
.about .body-copy{margin-top:24px}
.about .btn-more{margin-top:38px}

/* approach / values */
.approach{top:1220px;height:554px}
.approach .dark{left:0;top:0;width:600px;height:554px;background:radial-gradient(circle at 70% 55%,#1d4b74 0%,#0b2d4e 45%,#05213d 100%)}
.approach .light{left:600px;top:0;width:600px;height:554px;background:linear-gradient(120deg,#e9ecf0 0%,#f6f7f8 60%,#eef0f2 100%)}
.approach .col{top:87px;width:390px}
.approach .col.left{left:173px}
.approach .col.left .kicker,.approach .col.left .heading,.approach .col.left .body-copy{color:#fff}
.approach .col.right{left:638px}
.approach .body-copy{margin-top:22px}
.bridge-band{left:293px;top:317px;width:614px;height:156px;background:linear-gradient(90deg,rgba(255,255,255,.55) 0%,rgba(255,255,255,.25) 50%,rgba(11,62,111,.25) 52%,rgba(169,201,238,.5) 100%);border-radius:40% 60% 50% 30%}

/* culture */
.culture{top:1774px;height:595px;background:var(--paper)}
.culture .text{left:173px;top:124px;width:390px}
.culture .body-copy{margin-top:24px}
.culture .btn-more{margin-top:38px}
.photo-frame{left:628px;top:99px;width:403px;height:380px;border:5px solid #fff;border-radius:14px;box-shadow:0 6px 22px rgba(0,0,0,.25);background:linear-gradient(135deg,#c9ced4 0%,#9aa3ad 40%,#6b7988 70%,#2f3b48 100%)}
.hex{width:84px;height:84px}

/* looking for */
.looking{top:2369px;height:730px;background:var(--mist)}
.looking .title{left:0;width:1200px;top:78px;text-align:center}
.cycle{left:80px;top:2369px}
.wanted-list{left:604px;top:216px;width:424px}
.wanted-item{position:relative;height:105px;padding-left:58px}
.wanted-item svg{position:absolute;left:0;top:8px}
.wanted-item h3{font-size:19px;font-weight:500;line-height:1}
.wanted-item p{font-size:12.5px;line-height:22px;margin-top:8px;text-align:justify}
.t-navy{color:var(--brand-blue)}.t-blue{color:var(--mid-blue)}.t-plum{color:var(--plum)}.t-light{color:#9cc2ee}

/* footer */
.site-footer{top:3099px;height:553px;background:var(--navy-deep)}
.site-footer .brand-mark{left:173px;top:250px;font-size:42px;letter-spacing:1px}
.site-footer .brand-mark small{display:block;font-size:21px;letter-spacing:15px;margin-top:10px}
.foot-nav{left:530px;top:110px;list-style:none}
.foot-nav li{font-size:15px;color:#fff;line-height:36px}
.contact{left:700px;width:340px}
.contact .ico{position:absolute;left:0;top:0;width:51px;height:51px;border-radius:50%;background:#fff;display:flex;align-items:center;justify-content:center}
.contact .lbl{position:absolute;left:68px;top:0;color:#fff;font-size:15px}
.contact .val{position:absolute;left:68px;top:22px;color:#fff;font-size:21px;font-weight:500;line-height:27px;width:280px}
.rule{left:173px;top:443px;width:854px;height:1px;background:#8a97a6}
.copyright{left:0;width:1200px;top:488px;text-align:center;color:#fff;font-size:14px}
</style>
</head>
<body>

<header class="hero">
  <div class="globe abs" role="img" aria-label="Glowing wireframe globe of connected nodes"></div>
  <div class="brand-mark abs">HARLOW<small>VECTORS</small></div>
  <nav class="main-nav abs">
    <a href="#">HOME</a><a href="#">ABOUT</a><a href="#">SOLUTIONS</a><a href="#">FUNDS</a><a href="#">NEWS</a><a href="#">CONTACT</a>
  </nav>
  <a class="btn-login abs" href="#">CLIENT LOGIN</a>
  <h1 class="hero-title abs"><span class="small">SYSTEMATIC</span><span class="big">HEDGE FUND</span></h1>
  <p class="hero-lede abs">Duis aute irure dolor in reprehenderit in voluptate velit esse cillum dolore eu fugiat nulla pariatur.</p>
  <div class="slider-dots abs"><span></span><span></span><span></span></div>
</header>

<section class="about">
  <div class="bridge-art abs" role="img" aria-label="Blue node-and-strut bridge illustration"></div>
  <div class="text abs">
    <div class="kicker">ABOUT</div>
    <h2 class="heading">HARLOW VECTORS</h2>
    <p class="body-copy">Lorem ipsum dolor sit amet, consectetur adipiscing elit, sed do eiusmod tempor incididunt ut labore et dolore magna aliqua. Ut enim ad minim veniam, quis nostrud exercitation ullamco laboris nisi ut aliquip ex ea commodo consequat. Duis aute irure dolor in reprehenderit in voluptate velit esse cillum dolore eu fugiat nulla pariatur. Excepteur sint occaecat cupidatat non proident, sunt in culpa qui officia deserunt mollit anim id est laborum.</p>
    <a class="btn-more" href="#">READ MORE</a>
  </div>
</section>

<section class="approach">
  <div class="dark abs" role="img" aria-label="Dark blue photo of a hand holding a digital globe"></div>
  <div class="light abs"></div>
  <div class="bridge-band abs" role="img" aria-label="Bridge truss illustration, white on the left and blue on the right"></div>
  <div class="col left abs">
    <div class="kicker">ABOUT</div>
    <h2 class="heading">HARLOW APPROACH</h2>
    <p class="body-copy">Lorem ipsum dolor sit amet, consectetur adipiscing elit, sed do eiusmod tempor incididunt ut labore et dolore magna aliqua. Ut enim ad minim veniam, quis nostrud exercitation ullamco laboris nisi ut aliquip ex ea commodo consequat.</p>
  </div>
  <div class="col right abs">
    <div class="kicker">OUR</div>
    <h2 class="heading">COMPANY VALUES</h2>
    <p class="body-copy">Lorem ipsum dolor sit amet, consectetur adipiscing elit, sed do eiusmod tempor incididunt ut labore et dolore magna aliqua. Ut enim ad minim veniam, quis nostrud exercitation ullamco laboris nisi ut aliquip ex ea commodo consequat.</p>
  </div>
</section>

<section class="culture">
  <div class="text abs">
    <div class="kicker">ABOUT</div>
    <h2 class="heading">OUR CULTURE</h2>
    <p class="body-copy">Lorem ipsum dolor sit amet, consectetur adipiscing elit, sed do eiusmod tempor incididunt ut labore et dolore magna aliqua. Ut enim ad minim veniam, quis nostrud exercitation ullamco laboris nisi ut aliquip ex ea commodo consequat. Duis aute irure dolor in reprehenderit in voluptate velit esse cillum dolore eu fugiat nulla pariatur. Excepteur sint occaecat cupidatat non proident, sunt in culpa qui officia deserunt mollit anim id est laborum.</p>
    <a class="btn-more" href="#">READ MORE</a>
  </div>
  <div class="photo-frame abs" role="img" aria-label="Photo of hands reviewing financial charts and a tablet on a desk"></div>
  <svg class="hex abs" style="left:588px;top:134px" viewBox="0 0 84 84"><polygon points="42,2 78,22 78,62 42,82 6,62 6,22" fill="var(--brand-blue)" stroke="#fff" stroke-width="4"/><rect x="28" y="30" width="28" height="20" fill="none" stroke="#fff" stroke-width="2.5"/><polyline points="32,45 39,39 44,43 52,34" fill="none" stroke="#fff" stroke-width="2"/><line x1="42" y1="50" x2="42" y2="58" stroke="#fff" stroke-width="2.5"/></svg>
  <svg class="hex abs" style="left:588px;top:247px" viewBox="0 0 84 84"><polygon points="42,2 78,22 78,62 42,82 6,62 6,22" fill="var(--mid-blue)" stroke="#fff" stroke-width="4"/><ellipse cx="36" cy="30" rx="10" ry="4" fill="none" stroke="#fff" stroke-width="2.5"/><path d="M26 30v18c0 2 4 4 10 4M46 30v6" fill="none" stroke="#fff" stroke-width="2.5"/><circle cx="49" cy="47" r="9" fill="none" stroke="#fff" stroke-width="2.5"/></svg>
  <svg class="hex abs" style="left:588px;top:360px" viewBox="0 0 84 84"><polygon points="42,2 78,22 78,62 42,82 6,62 6,22" fill="var(--plum)" stroke="#fff" stroke-width="4"/><rect x="27" y="38" width="18" height="10" rx="5" transform="rotate(-45 36 43)" fill="none" stroke="#fff" stroke-width="2.5"/><rect x="39" y="36" width="18" height="10" rx="5" transform="rotate(-45 48 41)" fill="none" stroke="#fff" stroke-width="2.5"/></svg>
</section>

<section class="looking">
  <div class="title abs">
    <div class="kicker">WHAT</div>
    <h2 class="heading">WE ARE LOOKING FOR</h2>
  </div>
  <svg class="abs" style="left:0;top:0" width="560" height="730" viewBox="0 0 560 730">
    <circle cx="244" cy="457" r="156" fill="none" stroke="var(--brand-blue)" stroke-width="3" stroke-dasharray="2 6" stroke-linecap="round"/>
    <text x="244" y="468" text-anchor="middle" font-family="Jost, sans-serif" font-weight="600" font-size="32" fill="var(--brand-blue)">HARLOW</text>
    <text x="244" y="496" text-anchor="middle" font-family="Jost, sans-serif" font-weight="600" font-size="16" letter-spacing="9" fill="var(--brand-blue)">VECTORS</text>
    <circle cx="315" cy="319" r="9" fill="#fff" stroke="var(--brand-blue)" stroke-width="3"/>
    <circle cx="378" cy="387" r="9" fill="#fff" stroke="var(--mid-blue)" stroke-width="3"/>
    <circle cx="395" cy="472" r="9" fill="#fff" stroke="var(--plum)" stroke-width="3"/>
    <circle cx="353" cy="560" r="9" fill="#fff" stroke="var(--light-blue)" stroke-width="3"/>
    <g><circle cx="366" cy="259" r="37" fill="var(--brand-blue)" stroke="#2c73c4" stroke-width="4"/><polygon points="330,275 340,300 352,290" fill="#2c73c4"/><path d="M350 262l10-8 10 4 12-4M356 266l10 6 8-4" fill="none" stroke="#fff" stroke-width="2.5"/></g>
    <g><circle cx="446" cy="347" r="37" fill="var(--mid-blue)" stroke="#fff" stroke-width="3"/><polygon points="410,363 418,388 432,378" fill="var(--mid-blue)"/><circle cx="446" cy="342" r="9" fill="none" stroke="#fff" stroke-width="2.5"/><path d="M430 352v10M462 352v10" stroke="#fff" stroke-width="2.5"/></g>
    <g><circle cx="475" cy="470" r="37" fill="var(--plum)" stroke="#fff" stroke-width="3"/><polygon points="436,470 446,460 446,480" fill="var(--plum)"/><circle cx="475" cy="468" r="12" fill="none" stroke="#fff" stroke-width="2.5"/><circle cx="475" cy="468" r="4" fill="#fff"/></g>
    <g><circle cx="426" cy="582" r="37" fill="var(--light-blue)" stroke="#fff" stroke-width="3"/><polygon points="388,568 398,592 410,580" fill="var(--light-blue)"/><circle cx="426" cy="582" r="14" fill="none" stroke="#fff" stroke-width="2.5"/><circle cx="426" cy="582" r="6" fill="none" stroke="#fff" stroke-width="2.5"/></g>
  </svg>
  <div class="wanted-list abs">
    <div class="wanted-item"><svg width="38" height="38" viewBox="0 0 38 38"><circle cx="19" cy="19" r="19" fill="var(--brand-blue)"/><polyline points="11,19 17,25 28,13" fill="none" stroke="#fff" stroke-width="4"/></svg><h3 class="t-navy">NEMO ENIM IPSAM</h3><p>Lorem ipsum dolor sit amet, consectetur adipiscing elit, sed do eiusmod tempor incididunt ut labore et dolorem.</p></div>
    <div class="wanted-item"><svg width="38" height="38" viewBox="0 0 38 38"><circle cx="19" cy="19" r="19" fill="var(--mid-blue)"/><polyline points="11,19 17,25 28,13" fill="none" stroke="#fff" stroke-width="4"/></svg><h3 class="t-blue">NEMO ENIM IPSAM</h3><p>Lorem ipsum dolor sit amet, consectetur adipiscing elit, sed do eiusmod tempor incididunt ut labore et dolorem.</p></div>
    <div class="wanted-item"><svg width="38" height="38" viewBox="0 0 38 38"><circle cx="19" cy="19" r="19" fill="var(--plum)"/><polyline points="11,19 17,25 28,13" fill="none" stroke="#fff" stroke-width="4"/></svg><h3 class="t-plum">NEMO ENIM IPSAM</h3><p>Lorem ipsum dolor sit amet, consectetur adipiscing elit, sed do eiusmod tempor incididunt ut labore et dolorem.</p></div>
    <div class="wanted-item"><svg width="38" height="38" viewBox="0 0 38 38"><circle cx="19" cy="19" r="19" fill="var(--light-blue)"/><polyline points="11,19 17,25 28,13" fill="none" stroke="#fff" stroke-width="4"/></svg><h3 class="t-light">NEMO ENIM IPSAM</h3><p>Lorem ipsum dolor sit amet, consectetur adipiscing elit, sed do eiusmod tempor incididunt ut labore et dolorem.</p></div>
  </div>
</section>

<footer class="site-footer">
  <div class="brand-mark abs">HARLOW<small>VECTORS</small></div>
  <ul class="foot-nav abs">
    <li>HOME</li><li>ABOUT</li><li>SOLUTIONS</li><li>FUNDS</li><li>POLICIES</li><li>NEWS</li><li>CONTACT</li>
  </ul>
  <div class="contact abs" style="top:104px">
    <div class="ico"><svg width="26" height="26" viewBox="0 0 24 24"><path d="M6 3l3 4-2 2c1 3 4 6 7 7l2-2 4 3-2 3C11 20 4 13 3 5z" fill="none" stroke="var(--navy-deep)" stroke-width="1.5"/></svg></div>
    <div class="lbl">PHONE:</div><div class="val">(+44) 7700 900418</div>
  </div>
  <div class="contact abs" style="top:190px">
    <div class="ico"><svg width="26" height="20" viewBox="0 0 26 20"><rect x="1" y="1" width="24" height="18" fill="none" stroke="var(--navy-deep)" stroke-width="1.5"/><polyline points="1,1 13,11 25,1" fill="none" stroke="var(--navy-deep)" stroke-width="1.5"/></svg></div>
    <div class="lbl">MAIL:</div><div class="val">ll@harlow-vectors.example</div>
  </div>
  <div class="contact abs" style="top:287px">
    <div class="ico"><svg width="22" height="28" viewBox="0 0 22 28"><path d="M11 27C5 19 2 14 2 10a9 9 0 0 1 18 0c0 4-3 9-9 17z" fill="none" stroke="var(--navy-deep)" stroke-width="1.5"/><circle cx="11" cy="10" r="3.5" fill="none" stroke="var(--navy-deep)" stroke-width="1.5"/></svg></div>
    <div class="lbl">ADDRESS:</div><div class="val" style="font-weight:400">14 Fenmoor Lane, Ashmere, AS2 4QT</div>
  </div>
  <div class="rule abs"></div>
  <p class="copyright abs">Copyrights @ 2021 Harlow Vectors. All Rights Reserved.</p>
</footer>

</body>
</html>
```